Sunny Ladle Kitchen April Competition

The website slider is 990 X 225 pixels to fit in with this website www.sunnyladlekitchen.com.au

We would love a fun, lively, food-oriented slider created for Sunny Ladle Kitchen website. Sunny Ladle Kitchen is a central place where people who love food, cooking for their family and friends, and sharing recipes can hang out. We'd like the sliders to be simple, bright and to entice people to click on the link.

The banner ad needs to feature the Coastal Readers' Monthly cookbooks, and to use a colour scheme that also works with the existing website.

A slider in March was used to promote a similar competition which I will upload as inspiration, along with the image of the cook books to use.

Main text: Add your best mid-week meal recipes to win one of 8 cookbook sets!
Smaller text: The 8 best recipes as chosen by Sunny Ladle Kitchen editors will win.

```html
<!DOCTYPE html>
<html lang="en">
<head>
<meta charset="utf-8">
<title>Sunny Ladle Kitchen April Competition</title>
<link href="https://fonts.googleapis.com/css2?family=Arimo:wght@400;700&display=swap" rel="stylesheet">
<style>
  :root {
    --band-blue: #0a78bd;
    --grad-start: #0d86c8;
    --grad-end: #02b6cd;
    --ribbon-cream: #f6f3ee;
    --cover-teal: #19b3c9;
    --photo-tone-a: #e7d9c4;
    --photo-tone-b: #c96a4a;
    --accent-yellow: #f7ea6c;
    --text-white: #ffffff;
  }
  html, body {
    margin: 0;
    padding: 0;
    overflow: hidden;
    background: #ffffff;
  }
  .slider {
    position: relative;
    width: 1200px;
    height: 303px;
    overflow: hidden;
    background: linear-gradient(90deg, var(--grad-start) 0%, var(--grad-end) 100%);
    font-family: "Arimo", Arial, sans-serif;
  }
  .side-band {
    position: absolute;
    left: 0;
    top: 0;
    width: 112px;
    height: 303px;
    background: var(--band-blue);
  }
  .bookmark {
    position: absolute;
    left: 111px;
    top: 0;
    width: 237px;
    height: 303px;
  }
  .cookbook {
    position: absolute;
    left: 154px;
    top: 7px;
    width: 167px;
    height: 220px;
    background: var(--cover-teal);
    box-shadow: 0 1px 3px rgba(0,0,0,0.25);
    color: var(--text-white);
    text-align: center;
  }
  .cookbook-brand {
    margin-top: 9px;
    font-size: 9px;
    font-weight: 700;
    letter-spacing: 0.2px;
  }
  .cookbook-title {
    margin-top: 16px;
    font-size: 26px;
    font-weight: 400;
    line-height: 1;
  }
  .cookbook-subtitle {
    margin-top: 5px;
    font-size: 8px;
  }
  .cookbook-photo {
    position: absolute;
    left: 0;
    top: 90px;
    width: 167px;
    height: 120px;
    background: radial-gradient(ellipse at 50% 55%, var(--photo-tone-b) 0%, var(--photo-tone-a) 55%, var(--cover-teal) 90%);
  }
  .headline {
    position: absolute;
    left: 560px;
    top: 55px;
    width: 610px;
    margin: 0;
    text-align: center;
    color: var(--text-white);
    font-size: 40px;
    font-weight: 700;
    line-height: 56px;
    letter-spacing: -0.3px;
  }
  .headline-accent {
    color: var(--accent-yellow);
    font-size: 55px;
  }
  .fine-print {
    position: absolute;
    left: 540px;
    top: 251px;
    width: 650px;
    margin: 0;
    text-align: center;
    color: var(--text-white);
    font-size: 16.5px;
    font-weight: 700;
  }
</style>
</head>
<body>
  <div class="slider">
    <div class="side-band"></div>
    <svg class="bookmark" viewBox="0 0 237 303" aria-hidden="true">
      <polygon points="0,0 237,0 237,303 229,303 118,229 8,303 0,303" fill="var(--ribbon-cream)"/>
    </svg>
    <div class="cookbook">
      <div class="cookbook-brand">Coastal Readers' Monthly</div>
      <div class="cookbook-title">fresh bowls</div>
      <div class="cookbook-subtitle">from simple to spectacular</div>
      <div class="cookbook-photo" role="img" aria-label="Photo of a bowl of fresh salad on the cookbook cover"></div>
    </div>
    <h1 class="headline"><span class="headline-accent">Add</span> your best mid-week<br>meal recipes to win one of<br>8 cookbook sets!</h1>
    <p class="fine-print">The 8 best recipes as chosen by Sunny Ladle Kitchen editors will win.</p>
  </div>
</body>
</html>
```